Business Card design

Keen on a very modern design with using the red star as a feature point preferably will have it printed with red foiling.

Target Market(s)

Cosmetics

Industry/Entity Type

Cosmetics

Contact Information for Business Card

Marcie Budd
Director
9 Frey Avenue
Doveton West Victoria
Australia 3618
marcie@glowpactsupply.com.au

Font styles to use
Sans Serif

Colors
ec1f27
000000

Requirements
Must have
• Keen on some red stars on back with black background and I may get the red components printed as red foiling potentially

```html
<!DOCTYPE html>
<html lang="en">
<head>
<meta charset="utf-8">
<title>Glowpact Business Card</title>
<link rel="stylesheet" href="https://fonts.googleapis.com/css2?family=Open+Sans:wght@400;700;800&display=swap">
<style>
  :root {
    --brand-red: #ec1f27;
    --brand-black: #000000;
    --card-dark: #1f1d1d;
    --card-light: #f7f7f7;
    --text-grey: #4a4a4a;
    --backdrop: #ebebeb;
  }
  * { box-sizing: border-box; margin: 0; padding: 0; }
  html, body {
    width: 1200px;
    height: 900px;
    overflow: hidden;
    background: var(--backdrop);
    font-family: "Open Sans", Arial, sans-serif;
  }
  .card-set {
    position: absolute;
    inset: 0;
    display: flex;
    align-items: center;
    justify-content: center;
    gap: 60px;
  }
  .card {
    position: relative;
    width: 500px;
    height: 286px;
    box-shadow: 0 10px 28px rgba(0,0,0,0.14);
  }
  .card--front { background: var(--card-light); }
  .card--back {
    background: var(--card-dark);
    display: flex;
    align-items: center;
    justify-content: center;
  }

  .contact {
    position: absolute;
    left: 34px;
    top: 30px;
    width: 200px;
    color: var(--text-grey);
    font-size: 11px;
    line-height: 1.45;
  }
  .contact__name {
    color: var(--brand-red);
    font-weight: 700;
    font-size: 13px;
    letter-spacing: 0.04em;
    text-transform: uppercase;
    line-height: 1.2;
  }
  .contact__role { font-size: 11px; margin-bottom: 22px; }
  .contact__address { margin-bottom: 4px; }
  .contact__line {
    display: flex;
    align-items: center;
    gap: 7px;
    white-space: nowrap;
  }
  .contact__icon { width: 9px; height: 9px; fill: var(--brand-red); flex: none; }

  .wordmark {
    display: flex;
    align-items: center;
    gap: 8px;
    font-family: "Open Sans", Arial, sans-serif;
    font-weight: 800;
    letter-spacing: -0.02em;
    line-height: 1;
    white-space: nowrap;
  }
  .wordmark__dot {
    width: 0.45em;
    height: 0.45em;
    border-radius: 50%;
    background: var(--brand-red);
    flex: none;
  }
  .card--front .wordmark {
    position: absolute;
    right: 34px;
    top: 176px;
    font-size: 38px;
    color: var(--brand-black);
  }
  .card--back .wordmark {
    font-size: 50px;
    color: #ffffff;
  }
</style>
</head>
<body>
  <main class="card-set">
    <section class="card card--front" aria-label="Business card front">
      <div class="contact">
        <p class="contact__name">Marcie Budd</p>
        <p class="contact__role">Director</p>
        <p class="contact__address">9 Frey Avenue<br>Doveton West Victoria<br>Australia 3618</p>
        <p class="contact__line">
          <svg class="contact__icon" viewBox="0 0 24 24" aria-hidden="true"><path d="M6.6 10.8a15.1 15.1 0 0 0 6.6 6.6l2.2-2.2c.3-.3.7-.4 1-.2 1.1.4 2.3.6 3.6.6.6 0 1 .4 1 1V20c0 .6-.4 1-1 1A17 17 0 0 1 3 4c0-.6.4-1 1-1h3.5c.6 0 1 .4 1 1 0 1.3.2 2.5.6 3.6.1.3 0 .7-.2 1z"/></svg>
          555 214 307
        </p>
        <p class="contact__line">
          <svg class="contact__icon" viewBox="0 0 24 24" aria-hidden="true"><path d="M2 5h20v14H2z M3 6l9 7 9-7"/></svg>
          marcie@glowpactsupply.com.au
        </p>
      </div>
      <div class="wordmark"><span class="wordmark__dot"></span>Glowpact</div>
    </section>

    <section class="card card--back" aria-label="Business card back">
      <div class="wordmark"><span class="wordmark__dot"></span>Glowpact</div>
    </section>
  </main>
</body>
</html>
```